Field Notes for Business Risk Advisors

I am writing a best practice book for commercial lines insurance brokers. The subtitle is Nobody Promised The Trail Was Flat. So I want a graphic of maybe someone hiking the summit. I posted an example but don't feel limited I just foudn something I liked.

This is a business book

I just mocked up an example. I dont want designers limited by my design. I am looking for juggling to be artistically displayed on the front cover. I incorporated my name into the logo but probably dont want that in my final design. Should just have my name and designations Marek Dallow, AAi, CWCP

Commercial Insurance Agents

Insurance

Sans Serif

• Must have the title of the book
Field Notes
for Business Risk
Advisors

Also the sub title Nobody Promised The Trail Was Flat

My Name on front cover Marek Dallow, AAI, CWCP

Book Cover should be black. I uploaded a copy of my work comp playbook for my desired color scehme.

My Lantern Logo on front cover and Tidewell logo on back cover
• Color should be black gray adn red using color from my logo.

```html
<!DOCTYPE html>
<html lang="en">
<head>
<meta charset="utf-8">
<title>Field Notes for Business Risk Advisors – Book Cover</title>
<link rel="stylesheet" href="https://fonts.googleapis.com/css2?family=Oswald:wght@500;600;700&display=swap">
<style>
  :root {
    --stage-light: #fbfbfb;
    --stage-mid: #e6e6e6;
    --stage-dark: #cfcfcf;
    --cover-black: #0b0b0b;
    --band-black: #040404;
    --bar-gray: #1e1e1e;
    --bar-gray-soft: #272727;
    --glow-core: #fffaf0;
    --glow-warm: #cdbb98;
    --title-white: #ffffff;
    --byline-tan: #e2cda4;
    --accent-red: #c8102e;
  }
  html, body {
    margin: 0;
    padding: 0;
    width: 1200px;
    height: 848px;
    overflow: hidden;
  }
  body {
    background: radial-gradient(ellipse at 50% 45%, var(--stage-light) 0%, var(--stage-mid) 65%, var(--stage-dark) 100%);
    font-family: "Oswald", "Arial Narrow", sans-serif;
  }
  .stage {
    position: relative;
    width: 1200px;
    height: 848px;
  }
  .book-cover {
    position: absolute;
    left: 375px;
    top: 74px;
    width: 450px;
    height: 700px;
    box-shadow: 0 18px 40px rgba(0,0,0,0.35);
  }
  .book-cover svg { display: block; }
  .cover-title {
    font-family: "Oswald", "Arial Narrow", sans-serif;
    font-weight: 600;
    font-size: 44px;
    fill: var(--title-white);
    letter-spacing: 0.5px;
  }
  .cover-subtitle {
    font-family: "Oswald", "Arial Narrow", sans-serif;
    font-weight: 600;
    font-size: 28px;
    fill: var(--title-white);
  }
  .cover-byline {
    font-family: "Oswald", "Arial Narrow", sans-serif;
    font-weight: 500;
    font-size: 21px;
    fill: var(--byline-tan);
  }
  .cover-byline-label { fill: var(--title-white); font-size: 14px; }
  .publisher-name {
    font-family: "Oswald", "Arial Narrow", sans-serif;
    font-weight: 500;
    font-size: 18px;
    letter-spacing: 1.5px;
    fill: var(--title-white);
  }
</style>
</head>
<body>
<main class="stage">
  <section class="book-cover" aria-label="Front cover: Field Notes for Business Risk Advisors">
    <svg width="450" height="700" viewBox="0 0 450 700" xmlns="http://www.w3.org/2000/svg">
      <defs>
        <radialGradient id="titleGlow" cx="0.5" cy="0.5" r="0.5">
          <stop offset="0" stop-color="#fffaf0" stop-opacity="1"/>
          <stop offset="0.35" stop-color="#cdbb98" stop-opacity="0.7"/>
          <stop offset="1" stop-color="#000" stop-opacity="0"/>
        </radialGradient>
        <linearGradient id="lightBeam" x1="0" y1="0" x2="1" y2="1">
          <stop offset="0" stop-color="#6f6a60" stop-opacity="0.15"/>
          <stop offset="0.6" stop-color="#8a8376" stop-opacity="0.55"/>
          <stop offset="1" stop-color="#6f6a60" stop-opacity="0.1"/>
        </linearGradient>
        <radialGradient id="jugglerFill" cx="0.5" cy="0.55" r="0.55">
          <stop offset="0" stop-color="#f6f0e2"/>
          <stop offset="0.6" stop-color="#bfb39a" stop-opacity="0.75"/>
          <stop offset="1" stop-color="#8a8068" stop-opacity="0.15"/>
        </radialGradient>
        <clipPath id="coverClip"><rect width="450" height="700"/></clipPath>
      </defs>

      <g clip-path="url(#coverClip)">
        <rect class="cover-base" width="450" height="700" fill="var(--cover-black)"/>

        <g class="cover-bars">
          <rect x="70" y="-40" width="70" height="320" fill="var(--bar-gray)" transform="rotate(-22 105 110)"/>
          <rect x="260" y="-60" width="60" height="240" fill="var(--bar-gray-soft)" transform="rotate(-22 280 60)"/>
          <rect x="360" y="20" width="40" height="300" fill="var(--bar-gray)" transform="rotate(-22 380 170)"/>
          <rect x="110" y="430" width="70" height="320" fill="var(--bar-gray)" transform="rotate(-22 145 590)"/>
          <rect x="330" y="500" width="60" height="260" fill="var(--bar-gray-soft)" transform="rotate(-22 360 630)"/>
        </g>

        <polygon class="cover-beam" points="0,250 400,60 450,150 450,340 60,520 0,520" fill="url(#lightBeam)"/>
        <ellipse class="cover-glow" cx="265" cy="380" rx="190" ry="140" fill="url(#titleGlow)"/>

        <g class="cover-title-block">
          <text class="cover-title" transform="translate(26 216) rotate(-25)">FIELD NOTES</text>
          <text class="cover-title" transform="translate(58 284) rotate(-25)">FOR BUSINESS RISK</text>
          <text class="cover-title" transform="translate(104 396) rotate(-25)">ADVISORS</text>
        </g>

        <ellipse class="cover-artwork" cx="350" cy="300" rx="62" ry="78" fill="url(#jugglerFill)" role="img" aria-label="Illustration of a businessman juggling balls in an arc above his head"/>

        <polygon class="subtitle-band" points="0,545 450,345 450,490 0,700" fill="var(--band-black)"/>

        <text class="cover-subtitle" transform="translate(34 596) rotate(-31)" textLength="320" lengthAdjust="spacingAndGlyphs">Nobody Promised The Trail Was Flat</text>
        <text class="cover-byline" transform="translate(210 560) rotate(-27)"><tspan class="cover-byline-label">by: </tspan>Marek Dallow, AAI, CWCP</text>

        <g class="publisher-mark" aria-label="Lantern">
          <circle cx="318" cy="655" r="7" fill="var(--accent-red)"/>
          <text class="publisher-name" x="332" y="662">Lantern</text>
        </g>
      </g>
    </svg>
  </section>
</main>
</body>
</html>
```